New Website for World Wide Charity (VELORA)

We need a dynamic web design for our brand new charity organisation that will be working worldwide. We will be funded by donations so need to attract people to donate.

What We Do
We work to optimise the wellbeing of the planet, the animals and all that live within. Our slogan is Achieving Vibrational Equilibrium.

We have included a Powerpoint document which may help you understand what we need, it is just an idea for structure and style, it is not set in stone so feel free to be as creative as you like!
Updates

Designs look the same

Target Market(s)

Adults 18+ with an interest in animal, environmental. Businesses that may like to support our natural world or already support our natural world.

Number of Pages Required

3 page

Colors

Designer to choose colors to be used in the design.

Requirements
Must have
• We need the website to be easy to use and understand.

Web pages will be Home, What We Do, Who We Are, Success Stories, What You Can Do (Blog section), Seek Help, Donate, Join.
Nice to have
• Natural feel, easy to navigate, Ideally the website will look natural and organic.

Natural colours, blues, greens, sand, gold, brown, grey, silver, Orange and yellow for impact.
Should not have
• Should not have a dark coloured theme.

```html
<!DOCTYPE html>
<html lang="en">
<head>
<meta charset="utf-8">
<title>VELORA – Help Raise World Vibration</title>
<link href="https://fonts.googleapis.com/css2?family=Fira+Sans+Condensed:wght@600;700&family=Roboto:wght@400;500&display=swap" rel="stylesheet">
<style>
:root{
  --bg:#e4dbe6;
  --navy:#333d86;
  --green:#1f7a35;
  --ring:#5b7bb8;
  --ink:#151515;
  --grey:#7a7a7a;
  --nav-ink:#1d1d2b;
}
*{margin:0;padding:0;box-sizing:border-box}
html,body{width:1200px;height:3226px;overflow:hidden;background:var(--bg)}
body{position:relative;font-family:"Roboto",Arial,sans-serif;color:var(--ink)}
.abs{position:absolute}
.hero-art{left:0;top:0;width:1200px;height:590px;
  background:
    radial-gradient(ellipse 260px 120px at 600px 560px,rgba(228,219,230,1),rgba(228,219,230,0) 100%),
    radial-gradient(ellipse 180px 220px at 600px 300px,rgba(214,190,214,.9),rgba(214,190,214,0) 100%),
    radial-gradient(ellipse 220px 140px at 1020px 340px,rgba(106,52,150,.85),rgba(106,52,150,0) 100%),
    radial-gradient(ellipse 200px 160px at 160px 320px,rgba(88,78,150,.75),rgba(88,78,150,0) 100%),
    radial-gradient(ellipse 260px 70px at 320px 150px,rgba(255,232,214,.9),rgba(255,232,214,0) 100%),
    radial-gradient(ellipse 300px 60px at 880px 505px,rgba(255,246,236,.95),rgba(255,246,236,0) 100%),
    linear-gradient(180deg,#e9e0ec 0%,#e7dbe8 18%,#cbbddc 28%,#8f84c0 38%,#7a6db4 50%,#9d8cc6 60%,#d4c2dc 72%,#eddfe6 80%,var(--bg) 92%)}
.nav{top:58px;height:24px;font-size:15px;font-weight:500;color:var(--nav-ink);display:flex}
.nav a{color:inherit;text-decoration:none;margin-right:39px;white-space:nowrap}
.nav-left{left:185px}
.nav-right{left:703px}
.nav-rule{height:2px;background:var(--ring);top:82px}
.brand{left:536px;top:6px;width:128px;height:128px;border:2px solid var(--ring);border-radius:50%;
  display:flex;align-items:center;justify-content:center;font-size:17px;color:var(--navy);letter-spacing:.5px;background:rgba(236,228,238,.85)}
.utility{top:18px;left:858px;display:flex;gap:18px;font-size:13px;font-weight:500;color:var(--green)}
.utility span{display:flex;align-items:center;gap:5px}
.headline{top:598px;left:0;width:1200px;text-align:center;font-family:"Fira Sans Condensed",Arial,sans-serif;font-weight:700;font-size:43px;color:var(--navy);letter-spacing:.3px}
.lede{top:658px;left:0;width:1200px;text-align:center;font-size:15.5px;line-height:24px;color:var(--ink)}
.btn{display:flex;align-items:center;justify-content:center;gap:9px;background:var(--green);color:#fff;border-radius:20px;height:40px;font-size:15px;font-weight:500;text-decoration:none}
.btn-cta{left:500px;top:725px;width:200px}
.pillar{top:805px;width:290px;height:290px}
.pillar svg{position:absolute;left:0;top:0}
.pillar-label{position:absolute;left:0;top:130px;width:290px;text-align:center;font-size:26px;color:var(--navy);letter-spacing:.5px}
.btn-find{top:1106px;width:177px;font-size:14.5px}
.feature-art{width:460px;height:460px}
.feature-title{font-family:"Fira Sans Condensed",Arial,sans-serif;font-weight:600;font-size:44px;color:var(--ink);letter-spacing:.5px}
.feature-copy{font-size:15px;line-height:25.7px;color:var(--grey);white-space:nowrap}
.btn-read{width:144px}
.footer-col h3{font-size:18px;font-weight:500;color:var(--ink);margin-bottom:9px}
.footer-col a{display:block;font-size:15.5px;color:#555;text-decoration:none;line-height:30.5px}
.footer-brand{left:941px;top:2748px;width:150px;height:150px;border:2px solid var(--ring);border-radius:50%;display:flex;align-items:center;justify-content:center;font-size:19px;color:var(--navy);letter-spacing:.5px}
.footer-rule{left:95px;top:2937px;width:1007px;height:1px;background:#c9bccb}
.fine{font-size:15px;color:var(--ink)}
.footer-art{left:0;top:3006px;width:1200px;height:220px;
  background:
    radial-gradient(ellipse 90px 160px at 330px 230px,rgba(40,140,70,.85),rgba(40,140,70,0) 100%),
    radial-gradient(ellipse 300px 80px at 800px 60px,rgba(140,150,215,.6),rgba(140,150,215,0) 100%),
    linear-gradient(180deg,var(--bg) 0%,#cfc6e4 18%,#a8a6dc 38%,#7b7cc8 60%,#5a5bb0 80%,#44449a 100%)}
</style>
</head>
<body>

<div class="abs hero-art" role="img" aria-label="Misty purple mountain lake landscape with birds, trees and a soaring eagle reflected in the water"></div>

<nav class="abs nav nav-left"><a href="#">HOME</a><a href="#">WHAT WE DO</a><a href="#">WHO WE ARE</a></nav>
<div class="abs nav-rule" style="left:181px;width:320px"></div>
<nav class="abs nav nav-right"><a href="#">SUCCESS STORIES</a><a href="#" style="margin-right:0">WHAT YOU CAN DO</a></nav>
<div class="abs nav-rule" style="left:699px;width:320px"></div>

<div class="abs brand">VELORA</div>

<div class="abs utility">
  <span><svg width="13" height="12" viewBox="0 0 24 22"><path d="M12 21 3 12a5.5 5.5 0 0 1 9-7 5.5 5.5 0 0 1 9 7z" fill="none" stroke="currentColor" stroke-width="2.4"/></svg>DONATE</span>
  <span><svg width="12" height="12" viewBox="0 0 24 24"><circle cx="12" cy="7" r="5" fill="currentColor"/><path d="M2 24c0-7 4-10 10-10s10 3 10 10z" fill="currentColor"/></svg>JOIN</span>
</div>

<h1 class="abs headline">HELP RAISE WORLD VIBRATION</h1>
<p class="abs lede">Lorem ipsum dolor sit amet, consectetur adipiscing elit, sed do eiusmodr incididunt<br>ut labore et dolore magna aliqua. Quis ipsum suspendisse ultrices</p>
<a class="abs btn btn-cta" href="#">MAKE A DIFFERENCE</a>

<!-- Pillars -->
<div class="abs pillar" style="left:108px">
  <svg width="290" height="290" viewBox="0 0 290 290">
    <defs><linearGradient id="pill-env" x1="0" y1="0" x2="0" y2="1"><stop offset="0" stop-color="#dfe9d6"/><stop offset=".2" stop-color="#7fae5c"/><stop offset=".55" stop-color="#3e8a3a"/><stop offset="1" stop-color="#2a6a2e"/></linearGradient></defs>
    <path d="M3.9 120.5A143 143 0 0 1 286.1 120.5" fill="none" stroke="#3f6a3a" stroke-width="5"/>
    <path d="M286.1 169.5A143 143 0 0 1 3.9 169.5" fill="none" stroke="#3f6a3a" stroke-width="5"/>
    <circle cx="145" cy="145" r="123" fill="url(#pill-env)" role="img" aria-label="Green pine forest"/>
    <rect x="0" y="122" width="290" height="50" fill="var(--bg)"/>
  </svg>
  <div class="pillar-label">ENVIRONMENT</div>
</div>
<div class="abs pillar" style="left:455px">
  <svg width="290" height="290" viewBox="0 0 290 290">
    <defs><linearGradient id="pill-ani" x1="0" y1="0" x2="0" y2="1"><stop offset="0" stop-color="#e6f1f8"/><stop offset=".35" stop-color="#d8dfe0"/><stop offset=".5" stop-color="#a99a82"/><stop offset=".75" stop-color="#8c7656"/><stop offset="1" stop-color="#c09a50"/></linearGradient></defs>
    <path d="M3.9 120.5A143 143 0 0 1 286.1 120.5" fill="none" stroke="#cfe3f0" stroke-width="5"/>
    <path d="M286.1 169.5A143 143 0 0 1 3.9 169.5" fill="none" stroke="#8a6a3e" stroke-width="5"/>
    <circle cx="145" cy="145" r="123" fill="url(#pill-ani)" role="img" aria-label="Giraffe, elephants, zebra and other wild animals together"/>
    <rect x="0" y="122" width="290" height="50" fill="var(--bg)"/>
  </svg>
  <div class="pillar-label">ANIMAL</div>
</div>
<div class="abs pillar" style="left:802px">
  <svg width="290" height="290" viewBox="0 0 290 290">
    <defs><radialGradient id="pill-hum" cx=".55" cy=".25" r=".8"><stop offset="0" stop-color="#fff4dc"/><stop offset=".3" stop-color="#f0c27a"/><stop offset=".6" stop-color="#c8842e"/><stop offset="1" stop-color="#8a5a22"/></radialGradient></defs>
    <path d="M3.9 120.5A143 143 0 0 1 286.1 120.5" fill="none" stroke="#f3eef4" stroke-width="5"/>
    <path d="M286.1 169.5A143 143 0 0 1 3.9 169.5" fill="none" stroke="#a8742e" stroke-width="5"/>
    <circle cx="145" cy="145" r="123" fill="url(#pill-hum)" role="img" aria-label="Family with arms outstretched in a golden sunset field"/>
    <rect x="0" y="122" width="290" height="50" fill="var(--bg)"/>
  </svg>
  <div class="pillar-label">HUMAN</div>
</div>

<a class="abs btn btn-find" href="#" style="left:165px">FIND OUT MORE <span>»</span></a>
<a class="abs btn btn-find" href="#" style="left:512px">FIND OUT MORE <span>»</span></a>
<a class="abs btn btn-find" href="#" style="left:859px">FIND OUT MORE <span>»</span></a>

<!-- Feature: Environment -->
<svg class="abs feature-art" style="left:108px;top:1252px" viewBox="0 0 460 460">
  <defs><linearGradient id="feat-env" x1="0" y1="0" x2=".3" y2="1"><stop offset="0" stop-color="#8a8a98"/><stop offset=".15" stop-color="#e4b58a"/><stop offset=".3" stop-color="#9fb0b8"/><stop offset=".48" stop-color="#6f8a3c"/><stop offset=".72" stop-color="#4f6e2c"/><stop offset="1" stop-color="#9a968c"/></linearGradient></defs>
  <path d="M10.4 191.2A223 223 0 0 1 449.6 191.2" fill="none" stroke="var(--ring)" stroke-width="3.5"/>
  <path d="M449.6 268.8A223 223 0 0 1 10.4 268.8" fill="none" stroke="var(--ring)" stroke-width="3.5"/>
  <circle cx="230" cy="230" r="210" fill="url(#feat-env)" role="img" aria-label="Green mountain ridge with rocks at sunrise above misty valleys"/>
</svg>
<h2 class="abs feature-title" style="left:630px;top:1307px">ENVIRONMENT</h2>
<p class="abs feature-copy" style="left:632px;top:1376px">Lorem ipsum dolor sit amet, consectetur adipiscing elit, sdo eiusmod<br>tempor incididunt ut labore et dolore magna aliqua. Quu suspendisse<br>ultrices gravida. Risus commodo viverra maecenan lacus vel facilisis.<br>Lorem ipsum dolor sit amet, consectetur adiping elit, sed do eiusmod<br>tempor incididunt ut labore et dolore magna am suspendisse ultrices<br>gravida. Risus commodo viverra maecenas amsan lacus vel facilisis.<br>Lorem ipsum dolor sit amet, consectetur adipiscing elit, sdo eiusmod<br>tempor incididunt ut labore et dolore magna aliqua.</p>
<a class="abs btn btn-read" href="#" style="left:632px;top:1608px">READ MORE</a>

<!-- Feature: Animal -->
<svg class="abs feature-art" style="left:634px;top:1737px" viewBox="0 0 460 460">
  <defs><radialGradient id="feat-ani" cx=".6" cy=".45" r=".7"><stop offset="0" stop-color="#7a5e42"/><stop offset=".45" stop-color="#8b7252"/><stop offset=".8" stop-color="#8fa060"/><stop offset="1" stop-color="#a9b878"/></radialGradient></defs>
  <path d="M10.4 191.2A223 223 0 0 1 449.6 191.2" fill="none" stroke="var(--ring)" stroke-width="3.5"/>
  <path d="M449.6 268.8A223 223 0 0 1 10.4 268.8" fill="none" stroke="var(--ring)" stroke-width="3.5"/>
  <circle cx="230" cy="230" r="210" fill="url(#feat-ani)" role="img" aria-label="Brown bear with two cubs in green grass"/>
</svg>
<h2 class="abs feature-title" style="left:108px;top:1793px">ANIMAL</h2>
<p class="abs feature-copy" style="left:110px;top:1861px">Lorem ipsum dolor sit amet, consectetur adipiscing elit, sdo eiusmod<br>tempor incididunt ut labore et dolore magna aliqua. Quu suspendisse<br>ultrices gravida. Risus commodo viverra maecenan lacus vel facilisis.<br>Lorem ipsum dolor sit amet, consectetur adiping elit, sed do eiusmod<br>tempor incididunt ut labore et dolore magna am suspendisse ultrices<br>gravida. Risus commodo viverra maecenas amsan lacus vel facilisis.<br>Lorem ipsum dolor sit amet, consectetur adipiscing elit, sdo eiusmod<br>tempor incididunt ut labore et dolore magna aliqua.</p>
<a class="abs btn btn-read" href="#" style="left:110px;top:2094px">READ MORE</a>

<!-- Feature: Human -->
<svg class="abs feature-art" style="left:108px;top:2213px" viewBox="0 0 460 460">
  <defs>
    <linearGradient id="feat-hum" x1="0" y1="0" x2="0" y2="1"><stop offset="0" stop-color="#3f66b4"/><stop offset=".3" stop-color="#8ba6d6"/><stop offset=".5" stop-color="#6e7a90"/><stop offset=".65" stop-color="#e6e8ee"/><stop offset=".82" stop-color="#b9bcc6"/><stop offset="1" stop-color="#6c6a68"/></linearGradient>
    <radialGradient id="feat-hum-glow" cx=".45" cy=".3" r=".18"><stop offset="0" stop-color="#d2242a" stop-opacity=".75"/><stop offset="1" stop-color="#d2242a" stop-opacity="0"/></radialGradient>
  </defs>
  <path d="M10.4 191.2A223 223 0 0 1 449.6 191.2" fill="none" stroke="var(--ring)" stroke-width="3.5"/>
  <path d="M449.6 268.8A223 223 0 0 1 10.4 268.8" fill="none" stroke="var(--ring)" stroke-width="3.5"/>
  <g role="img" aria-label="Hiker with raised arms on a summit above clouds and snowy peaks">
    <circle cx="230" cy="230" r="210" fill="url(#feat-hum)"/>
    <circle cx="230" cy="230" r="210" fill="url(#feat-hum-glow)"/>
  </g>
</svg>
<h2 class="abs feature-title" style="left:630px;top:2267px">HUMAN</h2>
<p class="abs feature-copy" style="left:632px;top:2336px">Lorem ipsum dolor sit amet, consectetur adipiscing elit, sdo eiusmod<br>tempor incididunt ut labore et dolore magna aliqua. Quu suspendisse<br>ultrices gravida. Risus commodo viverra maecenan lacus vel facilisis.<br>Lorem ipsum dolor sit amet, consectetur adiping elit, sed do eiusmod<br>tempor incididunt ut labore et dolore magna am suspendisse ultrices<br>gravida. Risus commodo viverra maecenas amsan lacus vel facilisis.<br>Lorem ipsum dolor sit amet, consectetur adipiscing elit, sdo eiusmod<br>tempor incididunt ut labore et dolore magna aliqua.</p>
<a class="abs btn btn-read" href="#" style="left:632px;top:2570px">READ MORE</a>

<!-- Footer -->
<div class="abs footer-col" style="left:100px;top:2772px"><h3>GET INVOLVED</h3><a href="#">Join Us</a><a href="#">Fundraise</a><a href="#">Donate</a><a href="#">Shop</a></div>
<div class="abs footer-col" style="left:382px;top:2772px"><h3>GET HELP</h3><a href="#">Contact Us</a><a href="#">Media</a></div>
<div class="abs footer-col" style="left:621px;top:2772px"><h3>LEGAL</h3><a href="#">Terms and Conditions</a><a href="#">Cookies</a><a href="#">Privacy Policy</a></div>
<div class="abs footer-brand">VELORA</div>
<div class="abs footer-rule"></div>
<p class="abs fine" style="left:95px;top:2954px">Charity Number : 123 456 789</p>
<p class="abs fine" style="right:97px;top:2966px;font-size:14px">© 2021 VELORA. All Rights Reserved.</p>

<div class="abs footer-art" role="img" aria-label="Blue mountain forest silhouette with a figure standing with arms outstretched"></div>

</body>
</html>
```